Business card design for IT consulting company

Looking for a simple, modern, clean business card design.
Open to reworking our existing logo.

Attached is our current business cards which we do not like.
Ideally double sided with something simple on the back.
Rectangle / Horizonal only.
No rounded edges on the card.
White as the dominate color is preferred.

Target Market(s)

clients, legal, oil & gas, medical, professionals

Industry/Entity Type

IT, tech, consulting

Contact Information for Business Card

Name, Title, email, phone, cell, website

Font styles to use
Sans Serif

Requirements
Must have
• Clean design
Should not have
• loud colors or unusual fonts, etc

```html
<!DOCTYPE html>
<html lang="en">
<head>
<meta charset="utf-8">
<title>Tenvo Solutions – Business Card</title>
<link rel="stylesheet" href="https://fonts.googleapis.com/css2?family=Lato:wght@400;700;900&display=swap">
<style>
  :root {
    --backdrop: #76d3ea;
    --card-white: #ffffff;
    --card-black: #1b1b1b;
    --accent-red: #f04458;
    --deep-navy: #272a6e;
    --ink: #2b2b33;
    --muted: #55555f;
  }
  * { box-sizing: border-box; margin: 0; padding: 0; }
  html, body {
    width: 1200px; height: 1200px; overflow: hidden;
    background: var(--backdrop);
    font-family: "Lato", Arial, sans-serif;
  }
  .canvas { position: relative; width: 1200px; height: 1200px; }

  .card {
    position: absolute; left: 161px; width: 878px; height: 526px; overflow: hidden;
  }
  .card--front { top: 41px; background: var(--card-white); }
  .card--back {
    top: 625px; background: var(--card-black);
    display: flex; align-items: center; justify-content: center; gap: 28px;
  }

  .name-tab {
    position: absolute; left: 83px; top: 0; width: 58px; height: 154px;
    background: var(--accent-red); border-radius: 0 0 29px 29px;
  }
  .name-tab svg { position: absolute; left: 14px; bottom: 14px; width: 30px; height: 30px; }

  .identity { position: absolute; left: 157px; top: 88px; }
  .identity__name {
    font-weight: 700; font-size: 26px; letter-spacing: 1px; color: var(--ink); line-height: 1;
  }
  .identity__name span { color: var(--accent-red); font-weight: 400; }
  .identity__title { margin-top: 6px; font-size: 17px; color: var(--muted); }

  .contact-list { position: absolute; left: 83px; top: 284px; list-style: none; }
  .contact-list li {
    display: flex; align-items: center; gap: 6px; height: 40px;
    font-size: 24px; color: var(--ink);
  }
  .contact-list .icon {
    width: 32px; height: 32px; background: var(--accent-red);
    display: flex; align-items: center; justify-content: center; flex: none;
  }
  .contact-list .icon svg { width: 20px; height: 20px; }

  .brand {
    position: absolute; left: 605px; top: 60px; width: 217px; height: 217px;
    display: flex; align-items: center; justify-content: center; gap: 14px;
  }
  .brand__mark { width: 40px; height: 40px; background: var(--deep-navy); }
  .brand__name { font-weight: 900; font-size: 52px; color: var(--deep-navy); line-height: 1; }

  .base-band {
    position: absolute; left: 0; top: 460px; width: 480px; height: 18px;
    background: var(--deep-navy);
  }
  .corner-art { position: absolute; right: 0; bottom: 0; width: 355px; height: 261px; }

  .back-brand__mark { width: 110px; height: 110px; background: var(--accent-red); }
  .back-brand__name { font-weight: 900; font-size: 70px; color: var(--card-white); line-height: 1; }
</style>
</head>
<body>
<main class="canvas">

  <section class="card card--front" aria-label="Business card front">
    <div class="base-band" aria-hidden="true"></div>

    <svg class="corner-art" viewBox="0 0 355 261" role="img" aria-label="Decorative geometric corner in navy and red">
      <defs>
        <linearGradient id="cornerTone" x1="0" y1="1" x2="1" y2="0">
          <stop offset="0" stop-color="#f04458"/>
          <stop offset="1" stop-color="#272a6e"/>
        </linearGradient>
      </defs>
      <polygon points="0,261 355,0 355,261" fill="url(#cornerTone)"/>
    </svg>

    <div class="name-tab">
      <svg viewBox="0 0 24 24" aria-hidden="true">
        <circle cx="12" cy="7.5" r="5" fill="#fff"/>
        <path d="M2 23 C2 16 6 13.5 12 13.5 C18 13.5 22 16 22 23 Z" fill="#fff"/>
      </svg>
    </div>

    <div class="identity">
      <h1 class="identity__name">DANA <span>REYES</span></h1>
      <p class="identity__title">General Manager</p>
    </div>

    <ul class="contact-list">
      <li><span class="icon"><svg viewBox="0 0 24 24" aria-hidden="true"><path d="M6.6 10.8a15 15 0 0 0 6.6 6.6l2.2-2.2a1 1 0 0 1 1-.25 11.4 11.4 0 0 0 3.6.57 1 1 0 0 1 1 1V20a1 1 0 0 1-1 1A17 17 0 0 1 3 4a1 1 0 0 1 1-1h3.5a1 1 0 0 1 1 1c0 1.25.2 2.45.57 3.57a1 1 0 0 1-.25 1z" fill="#fff"/></svg></span>(555) 214-3308</li>
      <li><span class="icon"><svg viewBox="0 0 24 24" aria-hidden="true"><rect x="6" y="2" width="12" height="20" rx="2" fill="none" stroke="#fff" stroke-width="2"/><circle cx="12" cy="18" r="1.2" fill="#fff"/></svg></span>(555) 630-4471</li>
      <li><span class="icon"><svg viewBox="0 0 24 24" aria-hidden="true"><rect x="3" y="5" width="18" height="14" fill="#fff"/><polyline points="3,5 12,13 21,5" fill="none" stroke="#f04458" stroke-width="1.6"/></svg></span>Dana.reyes@tenvo.ca</li>
      <li><span class="icon"><svg viewBox="0 0 24 24" aria-hidden="true"><g fill="none" stroke="#fff" stroke-width="1.6"><circle cx="12" cy="12" r="9"/><ellipse cx="12" cy="12" rx="4" ry="9"/><line x1="3" y1="12" x2="21" y2="12"/><line x1="5" y1="7" x2="19" y2="7"/><line x1="5" y1="17" x2="19" y2="17"/></g></svg></span>www.tenvo.ca</li>
    </ul>

    <div class="brand">
      <span class="brand__mark" aria-hidden="true"></span>
      <span class="brand__name">Tenvo</span>
    </div>
  </section>

  <section class="card card--back" aria-label="Business card back">
    <span class="back-brand__mark" aria-hidden="true"></span>
    <span class="back-brand__name">Tenvo Solutions</span>
  </section>

</main>
</body>
</html>
```